Business Card & Word Docs from existing Logo

We need a business card with typical information plus layout to include electrical contractors license number, VONEL license and KMP license. We would like a word document layout for a proposal document, opening page with logo and design basic information; proposal to and proposal from and project name and number. Small basic single page letter for general documents. Email signature with logo.

We are an electrical, refrigeration and automation contractor. We work with reducing energy consumption for our customers and complex process solutions in electrical, refrigeration and automation.

Reason: Final changes/ revisions to designs.

Target Market(s)

Industrial and commercial businesses that require more than your average contractor.

Industry/Entity Type

Electrical

Requirements
Must have
• Propsal document must have a full opening page.

```html
<!DOCTYPE html>
<html lang="en">
<head>
<meta charset="UTF-8">
<title>Frostline Contracting – Proposal Cover</title>
<link rel="stylesheet" href="https://fonts.googleapis.com/css2?family=Source+Sans+3:wght@400;700&display=swap">
<style>
  :root {
    --paper: #ffffff;
    --green-pale: #cfe6d3;
    --green-soft: #7fbf8e;
    --green-mid: #4ea86a;
    --green-deep: #16914a;
    --brand-blue: #1c7fb5;
    --ink: #2b2f33;
    --rule: #1f5f86;
    --footer-text: #ffffff;
  }
  * { margin: 0; padding: 0; box-sizing: border-box; }
  html, body {
    width: 900px;
    height: 1200px;
    overflow: hidden;
    background: var(--paper);
  }
  .cover {
    position: relative;
    width: 900px;
    height: 1200px;
    overflow: hidden;
    font-family: "Source Sans 3", "Myriad Pro", Arial, sans-serif;
    background: linear-gradient(180deg,
      var(--paper) 0px,
      var(--paper) 360px,
      var(--green-pale) 470px,
      var(--green-soft) 600px,
      var(--green-mid) 820px,
      var(--green-deep) 1080px,
      var(--green-deep) 1200px);
  }
  .line-texture {
    position: absolute;
    left: 0;
    top: 0;
    width: 900px;
    height: 560px;
    background: radial-gradient(ellipse at 0% 0%,
      rgba(70, 110, 150, 0.10) 0%,
      rgba(70, 110, 150, 0.05) 40%,
      rgba(255, 255, 255, 0) 70%);
  }
  .brand {
    position: absolute;
    left: 318px;
    top: 278px;
    display: flex;
    align-items: center;
    gap: 16px;
  }
  .brand-dot {
    width: 64px;
    height: 64px;
    border-radius: 50%;
    background: var(--brand-blue);
  }
  .brand-name {
    font-weight: 700;
    font-size: 46px;
    line-height: 1;
    letter-spacing: 1px;
    color: var(--brand-blue);
    text-transform: uppercase;
  }
  .proposal-info {
    position: absolute;
    right: 95px;
    top: 540px;
    text-align: right;
    color: var(--ink);
  }
  .proposal-title {
    font-weight: 700;
    font-size: 25px;
    line-height: 32px;
  }
  .proposal-detail {
    font-weight: 400;
    font-size: 24px;
    line-height: 29px;
  }
  .footer-rule {
    position: absolute;
    left: 38px;
    right: 44px;
    top: 1140px;
    height: 1.5px;
    background: var(--rule);
  }
  .licences {
    position: absolute;
    left: 0;
    right: 30px;
    top: 1156px;
    display: flex;
    justify-content: center;
    align-items: center;
    color: var(--footer-text);
    font-size: 16.5px;
    line-height: 24px;
  }
  .licence + .licence {
    border-left: 1px solid rgba(255, 255, 255, 0.7);
    margin-left: 10px;
    padding-left: 10px;
  }
</style>
</head>
<body>
  <main class="cover">
    <div class="line-texture" role="img" aria-label="Fine curved line pattern sweeping across the top left corner"></div>

    <div class="brand">
      <span class="brand-dot"></span>
      <span class="brand-name">Frostline Contracting</span>
    </div>

    <section class="proposal-info">
      <h1 class="proposal-title">Test Proposal For A New Project</h1>
      <p class="proposal-detail">Location Unknown</p>
      <p class="proposal-detail">19st March 2011</p>
      <p class="proposal-detail">Ref QBMGORM</p>
    </section>

    <div class="footer-rule"></div>
    <footer class="licences">
      <span class="licence">Electrical Contractors License 12345</span>
      <span class="licence">KMP 1234567</span>
      <span class="licence">VONEL AA12345</span>
    </footer>
  </main>
</body>
</html>
```